Recruitment company website redesign

We're looking to redesign our current website, located at http://www.crestwayhire.com.au, to make it more FRESH, modern, easy-to-navigate, and user-friendly. Navigation should be very obvious, and buttons should be big. The design should be closer to the flat/clean look of Zorvik or Qelt9 rather than the somewhat older embossed look.

The design also needs to take into consideration that the coding will be responsive (mobile, tablet, etc.-friendly).

We'd like to see your work on two pages, and from there, we'll choose a designer that we will pay further to design the rest of the site. The two pages we will need are:

1. A home page, with the content detailed in the attached image home-outline.jpg. Keep in mind that this is a very rough outline with no design whatsoever, so please take those elements and create a beautiful page from it. Feel free to move the content around if necessary, as long as that's all on there. We're pretty open to whatever you think would look best.

Using high quality images could look great, and we'd purchase the perfect stock photos down the line, but for now just use any business-related images that aren't too cheesy (stay away from anything that looks too stock image-y like smiling actors).

2. A talent dashboard. This will live as a separate microsite; therefore, the design should be consistent with the home page but also be separate. Here, you have some more freedom with the design, but use our overall style and make it look like a user dashboard - very simple and easy to translate for responsive design.

There should be a horizontal menu that includes: "Edit Profile," "Apply for a Job," "WHS" (this will have a drop-down submenu), "My History" (also with a drop-down submenu), and "Contact."

Above that menu should be a place for users to sign in/out. Below the menu will be a welcome message and then a notice board for our updates.

Reason: Still haven't found the perfect design.

Hi designers,

We will make a decision Monday and let you know. Thanks for your submissions!

Industry/Entity Type

Business

Font styles to use
Sans Serif

Colors
33b7a4
f78f20
ffffff

Requirements
Must have
• Please use our current color scheme, fonts, and logo. Attached is our logo and style guidelines. Not included in those style guidelines is the orange we also incorporate into our designs, which is #ff9a00.

Also have a look at http://www.crestwayhire.com.au, http://www.crestwayhire.com.au/blog, and http://www.linkvora.com/crestwayhirerecruitment. We want to take our current look and just modernize it a bit.

```html
<!DOCTYPE html>
<html lang="en">
<head>
<meta charset="utf-8">
<title>Crestway Hire — Home</title>
<link rel="stylesheet" href="https://fonts.googleapis.com/css2?family=Roboto:wght@300;400;700&family=Roboto+Condensed:wght@300&display=swap">
<style>
:root{
  --teal:#0a9fb0;
  --teal-light:#5ec3cf;
  --nav-grey:#6e6f73;
  --bar-grey:#6d6e72;
  --text:#5d5e62;
  --text-dark:#333;
  --footer:#2f3035;
  --footer-line:#45464b;
  --footer-text:#c9cacd;
  --white:#fff;
}
*{margin:0;padding:0;box-sizing:border-box}
html,body{width:678px;height:1200px;overflow:hidden}
body{position:relative;background:var(--white);font-family:'Roboto',Arial,sans-serif;color:var(--text)}
.abs{position:absolute}

/* header */
.logo{left:21px;top:10px;font-weight:300;font-size:38px;color:var(--teal);letter-spacing:-1px}
.social{display:flex;gap:6px}
.social span{width:19px;height:19px;border-radius:50%;background:var(--teal)}
.social--top{right:37px;top:13px}
.top-phone{right:32px;top:36px;font-weight:300;font-size:18px;color:#444}

/* nav */
.main-nav{left:0;top:70px;width:678px;height:36px;background:var(--nav-grey)}
.main-nav a{position:absolute;top:0;height:36px;line-height:36px;color:var(--white);text-decoration:none;font-weight:300;font-size:16px}
.main-nav a.active{left:0;width:88px;background:var(--teal);text-align:center}

/* hero */
.hero-photo{left:0;top:106px;width:678px;height:316px;background:linear-gradient(180deg,#c9c8c4 0%,#8a8784 30%,#2a2b30 55%,#d8d3cf 78%,#e9e6e2 100%)}
.hero-box{left:13px;top:163px;width:300px;height:120px;background:rgba(235,235,235,.88);padding:16px 0 0 20px;font-weight:300;font-size:15px;line-height:16.6px;color:#222}
.hero-video{left:13px;top:283px;width:300px;height:31px;background:rgba(110,111,115,.9);color:var(--white);font-weight:300;font-size:15.5px;line-height:31px;padding-left:59px}
.hero-video svg{position:absolute;left:35px;top:8px}

/* action band */
.band{left:0;top:422px;width:678px;height:127px;background:var(--teal)}
.action{width:240px;text-align:center;color:var(--white)}
.action .ring{margin:0 auto;width:96px;height:96px;border-radius:50%;background:var(--white);padding:4px}
.action .ring div{width:88px;height:88px;border-radius:50%;border:3px solid var(--teal);background:#e8e8e8;display:flex;align-items:center;justify-content:center}
.action p{margin-top:12px;font-weight:300;font-size:21px}

/* browse */
.bar{top:563px;height:31px;color:var(--white);font-weight:300;font-size:17px;line-height:31px;padding-left:30px}
.bar svg{position:absolute;left:11px;top:11px}
.bar--browse{left:9px;width:457px;background:var(--bar-grey)}
.bar--featured{left:466px;width:206px;background:var(--teal-light)}
.job-group{font-size:8.4px;line-height:10.4px;color:var(--text)}
.job-group h3{font-size:8.4px;font-weight:700;color:#555}

.company{font-family:'Roboto',Arial,sans-serif;font-weight:700;font-size:15px;color:#444;width:90px;text-align:center}

/* footer */
.footer{left:0;top:916px;width:678px;height:284px;background:var(--footer)}
.footer h4{position:absolute;top:34px;font-weight:300;font-size:17px;color:var(--white);letter-spacing:-.3px}
.footer ul{position:absolute;top:63px;list-style:none;font-size:7.6px;line-height:10px;color:var(--footer-text)}
.footer .social span{background:#8c8d91}
.footer-rule{left:0;top:1110px;width:678px;height:1px;background:var(--footer-line)}
.legal{left:0;width:678px;text-align:center;font-size:7.4px;color:#8e8f93;line-height:10px}
.foot-phone{font-family:'Roboto Condensed',Arial,sans-serif;font-weight:300;font-size:19px;color:var(--footer-text)}
</style>
</head>
<body>

<header>
  <div class="abs logo">crestway<span style="margin-left:4px">hire</span></div>
  <div class="abs social social--top" aria-label="Social links"><span></span><span></span><span></span><span></span><span></span></div>
  <div class="abs top-phone">1-800-555-0142</div>
</header>

<nav class="abs main-nav">
  <a class="active" href="#">Home</a>
  <a href="#" style="left:127px">About</a>
  <a href="#" style="left:230px">Clients</a>
  <a href="#" style="left:338px">Candidates</a>
  <a href="#" style="left:477px">Blog</a>
  <a href="#" style="left:569px">Contact</a>
</nav>

<section>
  <div class="abs hero-photo" role="img" aria-label="Business people in suits seated in a row, waiting for interviews"></div>
  <div class="abs hero-box">Whether you are looking for your next career opportunity,or you are looking to recruit new people for your business. We believe in listening and tailoring our services to your needs.</div>
  <div class="abs hero-video">
    <svg width="15" height="15" viewBox="0 0 15 15"><circle cx="7.5" cy="7.5" r="7.5" fill="#fff"/><circle cx="7.5" cy="7.5" r="6" fill="#1a8fe0"/><path d="M5.8 4.3v6.4l5-3.2z" fill="#fff"/></svg>
    Click here to watch Video
  </div>
</section>

<section class="abs band"></section>
<div class="abs action" style="left:76px;top:388px">
  <div class="ring"><div>
    <svg width="44" height="44" viewBox="0 0 44 44"><path d="M22 4 40 13 22 22 4 13z" fill="#999"/><path d="M4 15 21 24V42L4 33z" fill="#777"/><path d="M40 15 23 24V42L40 33z" fill="#888"/></svg>
  </div></div>
  <p>FIND A JOB</p>
</div>
<div class="abs action" style="left:360px;top:388px">
  <div class="ring"><div>
    <svg width="50" height="40" viewBox="0 0 50 40"><rect x="8" y="4" width="34" height="24" rx="3" fill="#777"/><rect x="11" y="7" width="28" height="18" fill="#f3f3f3"/><path d="M2 31h46l-3 4H5z" fill="#777"/><path d="M28 14v7l2-2 1.5 3 1-.5-1.5-3h3z" fill="#555"/></svg>
  </div></div>
  <p>FIND EMPLOYEES</p>
</div>

<main>
  <div class="abs bar bar--browse"><svg width="8" height="9" viewBox="0 0 8 9"><path d="M0 0v9l8-4.5z" fill="#fff"/></svg>Browse Jobs</div>
  <div class="abs bar bar--featured"><svg width="8" height="9" viewBox="0 0 8 9"><path d="M0 0v9l8-4.5z" fill="#fff"/></svg>Featured Companies</div>

  <div class="abs job-group" style="left:15px;top:608px"><h3>Accounting / Finance</h3>General/Cost Acct (2866)<br>Banking/Financial (1885)<br>Audit &amp; Taxation (793)<br>Finance/Investment (345)</div>
  <div class="abs job-group" style="left:15px;top:670px"><h3>Admin / HR</h3>Clerical/Administrative (2662)<br>Human Resources (1845)<br>Secretarial (725)<br>Top Management (83)</div>
  <div class="abs job-group" style="left:15px;top:733px"><h3>Sales / Marketing</h3>Retail Sales (2479)<br>Marketing (2472)<br>Sales - Corporate (1352)<br>Telesales/Telemarketing (1072)<br>Sales - Eng/Tech/IT (590)<br>Sales - Financial Services (305)<br>Merchandising (261)</div>

  <div class="abs job-group" style="left:178px;top:608px"><h3>Computer / IT</h3>Software (3467)<br>Network/Sys/DB (1976)<br>Hardware (1726)</div>
  <div class="abs job-group" style="left:178px;top:660px"><h3>Engineering</h3>Mechanical/Automotive (6530)<br>Other Eng (5245)<br>Electrical Eng (2865)<br>Electronics Eng (1526)<br>Environmental (619)<br>Oil/Gas Eng (487)<br>Industrial Eng (373)<br>Chemical Eng (345)</div>
  <div class="abs job-group" style="left:178px;top:764px"><h3>Manufacturing</h3>Manufacturing (3713)<br>Maintenance (1636)<br>Purchasing (1085)<br>Quality Assurance (985)<br>Process Design &amp; Control (200)</div>
  <div class="abs job-group" style="left:178px;top:837px"><h3>Building / Construction</h3>Civil Eng/Construction (4003)<br>Architect/Interior (1161)<br>Property/Real Estate (554)<br>Quantity Survey (462)</div>

  <div class="abs job-group" style="left:332px;top:611px"><h3>Arts / Media / Comm</h3>Arts/Creative Design (1134)<br>Advertising (421)<br>Public Relations (234)<br>Entertainment (68)</div>
  <div class="abs job-group" style="left:332px;top:673px"><h3>Services</h3>Customer Service (8258)<br>Tech &amp; Helpdesk Support (1576)<br>Personal Care (1112)<br>Logistics/Supply Chain (616)<br>Security/Armed Forces (292)<br>Law/Legal Services (164)<br>Social Services (26)</div>
  <div class="abs job-group" style="left:332px;top:764px"><h3>Hotel / Restaurant</h3>F &amp; B (4734)<br>Hotel/Tourism (1956)</div>
  <div class="abs job-group" style="left:332px;top:805px"><h3>Education / Training</h3>Education (1367)<br>Training &amp; Dev. (486)</div>

  <div class="abs company" style="left:463px;top:626px">Marlow</div>
  <div class="abs company" style="left:573px;top:626px">Tessaro</div>
  <div class="abs company" style="left:463px;top:677px">Kaneda</div>
  <div class="abs company" style="left:573px;top:677px">Brightwell</div>
  <div class="abs company" style="left:463px;top:722px">Solvane</div>
  <div class="abs company" style="left:573px;top:722px">Orvik</div>
  <div class="abs company" style="left:463px;top:770px">Appgrid</div>
</main>

<footer class="abs footer">
  <h4 style="left:21px">NAVIGATION</h4>
  <ul style="left:22px"><li>Home</li><li>About Us</li><li>Clients</li><li>Candidates</li><li>Blog</li><li>Contact Us</li></ul>
  <h4 style="left:177px">LOCATIONS</h4>
  <ul style="left:176px">
    <li>Chicago, IL , New York, NY ,</li><li>Boston, MA , Providence, RI ,</li><li>Hartford, CT, Philadelphia, PA,</li><li>Washington D.C., San Francisco, CA,</li><li>Seattle, WA , San Diego, CA,</li><li>Los Angeles, CA, Las Vegas, NV,</li><li>Denver, CO.</li>
  </ul>
  <h4 style="left:362px">HELPS</h4>
  <ul style="left:362px"><li>Privacy Policy</li><li>Terms of Use</li><li>Take a tour</li><li>For Employers</li><li>For Employees</li></ul>
  <h4 style="left:540px">CONNECT</h4>
  <div class="abs social" style="left:538px;top:62px"><span></span><span></span><span></span><span></span><span></span></div>
  <div class="abs" style="left:541px;top:90px;font-size:9.5px;color:var(--white)">Crestway Hire</div>
  <div class="abs" style="left:541px;top:102px;font-size:7.4px;line-height:10px;color:var(--footer-text)">48 Harbour Lane,<br>Fairhaven, CT 06099</div>
  <div class="abs foot-phone" style="left:540px;top:127px">
    <svg width="18" height="18" viewBox="0 0 18 18" style="vertical-align:-2px;margin-right:3px"><circle cx="9" cy="9" r="8" fill="none" stroke="#c9cacd" stroke-width="1.2"/><path d="M6 4.5l1.6 2.3-.9 1.1c.5 1.2 1.3 2 2.4 2.5l1.1-.9 2.3 1.6-.8 1.5c-3.4-.3-6.3-3.2-6.6-6.6z" fill="#c9cacd"/></svg>012-555-0148
  </div>
</footer>
<div class="abs footer-rule"></div>
<div class="abs legal" style="top:1123px">©2013 CrestwayHire.com All Rights Reserved.</div>
<div class="abs legal" style="top:1143px">48 Harbour Lane • Fairhaven, CT 06099<br>Phone: 800-555-0142 • Fax: 860-555-0177</div>

</body>
</html>
```